ROLL UP CREATION

For a trade show we need three visuals to be seen see pdf file with slogans and photos. I expect from you a nice and attractive formatting that is urgent. the files must be in high definition for the printer. You will find enclosed the 3 visuals, photos the basic logo by adding the .com and the photo of the Rollup For a trade show we need to see the pdf file with slogans and photos. I expect from you a nice and attractive formatting that is urgent. the files must be in high definition for the printer. For a trade show we need to see the pdf file with slogans and photos. I expect from you a nice and attractive formatting that is urgent. the files must be in high definition for the printer. For a trade show we need to see the pdf file with slogans and photos. I expect from you a nice and attractive formatting that is urgent. the files must be in high definition for the printer. For a trade show we need to see the pdf file with slogans and photos. I expect from you a nice and attractive formatting that is urgent. the files must be in high definition for the printer. For a trade show we need to see the pdf file with slogans and photos. I expect from you a nice and attractive formatting that is urgent. the files must be in high definition for the printer. For a trade show we need to see the pdf file with slogans and photos. I expect from you a nice and attractive formatting that is urgent. the files must be in high definition for the printer. For a trade show we need to see the pdf file with slogans and photos. I expect from you a nice and attractive formatting that is urgent. the files must be in high definition for the printer. For a trade show we need to see the pdf file with slogans and photos. I expect from you a nice and attractive formatting that is urgent. the files must be in high definition for the printer. For a trade show we need to see the pdf file with slogans and photos. I expect from you a nice and attractive formatting that is urgent. the files must be in high definition for the printer.

Target Market(s)

Professional

Industry/Entity Type

Trade

Requirements
Must have
• the project the messages and the photos are chosen all the way to a nice and professional result. This is urgently the size of the rollup is 200/85.
Nice to have
• the bottom of the rollup on 40 cm must be just color because in an exhibition the visitors can not see the messages near the ground.
Should not have
• no green color

```html
<!DOCTYPE html>
<html lang="fr">
<head>
<meta charset="utf-8">
<title>Brikfolio – roll-ups salon</title>
<link rel="stylesheet" href="https://fonts.googleapis.com/css2?family=Quicksand:wght@500;600&display=swap">
<style>
  :root {
    --stage-bg: #e9e9ec;
    --brand-blue: #3a78bd;
    --brand-purple: #7b4f90;
    --frame-white: #ffffff;
    --frame-accent: #2f72bb;
    --text-light: #ffffff;
  }
  * { margin: 0; padding: 0; box-sizing: border-box; }
  html, body {
    width: 1200px; height: 1000px; overflow: hidden;
    background: var(--stage-bg);
    font-family: "Quicksand", "Trebuchet MS", sans-serif;
  }
  .stage { position: relative; width: 1200px; height: 1000px; }
  .rollup {
    position: absolute; top: 147px;
    width: 300px; height: 706px;
    overflow: hidden;
    color: var(--text-light);
    background: linear-gradient(180deg, var(--brand-blue) 0%, #4f6cb4 40%, #7a5aa6 62%, var(--brand-purple) 100%);
    box-shadow: 0 10px 30px rgba(0,0,0,.18);
  }
  .rollup--left { left: 90px; }
  .rollup--center { left: 450px; }
  .rollup--right { left: 810px; }
  .rollup__frame {
    position: absolute; left: 24px; top: 219px;
    width: 252px; height: 252px; border-radius: 50%;
    background: var(--frame-white);
    padding: 9px;
  }
  .rollup__photo {
    width: 100%; height: 100%; border-radius: 50%;
    border: 4px solid var(--frame-accent);
  }
  .rollup__photo--duo { background: radial-gradient(circle at 50% 45%, #d8b39a 0%, #8fa6c2 60%, #5d7596 100%); }
  .rollup__photo--seer { background: radial-gradient(circle at 50% 70%, #fbeedd 0%, #b98a5a 30%, #2a1e18 100%); }
  .rollup__photo--office { background: radial-gradient(circle at 45% 40%, #f1e3da 0%, #c9d3dc 60%, #7fa3bf 100%); }
  .brand {
    position: absolute; top: 38px; left: 24px;
    display: flex; align-items: center; gap: 10px;
    font-size: 27px; font-weight: 500; letter-spacing: .2px;
  }
  .brand__dot {
    width: 26px; height: 26px; border-radius: 50%;
    background: var(--text-light);
  }
  .slogan {
    position: absolute; left: 22px; width: 250px;
    font-size: 15px; font-weight: 500; line-height: 1.45;
  }
  .slogan--top { top: 120px; }
  .slogan--bottom { top: 545px; }
</style>
</head>
<body>
<main class="stage">

  <section class="rollup rollup--left">
    <div class="brand"><span class="brand__dot"></span>brikfolio.com</div>
    <p class="slogan slogan--top">La réalisation d’un DTG va étonner plus d’un copropriétaire!!</p>
    <div class="rollup__frame">
      <div class="rollup__photo rollup__photo--duo" role="img" aria-label="Photo : deux hommes étonnés penchés vers l'avant, lunettes sur le nez"></div>
    </div>
    <p class="slogan slogan--bottom">Le DTG, l´outil qui optimise vos charges et votre patrimoine...</p>
  </section>

  <section class="rollup rollup--center">
    <div class="brand"><span class="brand__dot"></span>brikfolio.com</div>
    <p class="slogan slogan--top">Nous ne pourrons pas prédire votre avenir...</p>
    <div class="rollup__frame">
      <div class="rollup__photo rollup__photo--seer" role="img" aria-label="Photo : voyante âgée, mains autour d'une boule de cristal lumineuse"></div>
    </div>
    <p class="slogan slogan--bottom">mais avec le DTG, celui de votre immeuble pour les 10 prochaines années !!</p>
  </section>

  <section class="rollup rollup--right">
    <div class="brand"><span class="brand__dot"></span>brikfolio.com</div>
    <p class="slogan slogan--top">Finis le stress pour la gestion de vos copropriétés...</p>
    <div class="rollup__frame">
      <div class="rollup__photo rollup__photo--office" role="img" aria-label="Photo : employée stressée derrière une pile de dossiers au bureau"></div>
    </div>
    <p class="slogan slogan--bottom">BRIKFOLIO le portail dédié aux professionnels de l´immobilier.</p>
  </section>

</main>
</body>
</html>
```